Business Card - connecting 2 souls and beggining the journey of self discovery

Logo on the front
with tag line

On the back list of services and contact details

Seminars
workshops
Coaching
podcasts

Daniel Porthwick
Health & Wellbeing Life Coach
0491 372 815
daniel@wovenpathwellness.example
wovenpathwellness.example

Industry/Entity Type

Life Coaching

Contact Information for Business Card

I like the use of colour from the logo to be used. I'm not a fan of white.

Requirements
Must have
• My tagline: The journey home starts with you
Nice to have
• Use of colour that is in the mind body soul logo

```html
<!DOCTYPE html>
<html lang="en">
<head>
<meta charset="utf-8">
<title>Woven Path Wellness – Business Card</title>
<link href="https://fonts.googleapis.com/css2?family=Montserrat:wght@600&family=Source+Sans+3:wght@300;400;700&family=Baloo+2:wght@700;800&family=Alfa+Slab+One&family=Roboto+Condensed:ital,wght@1,300&display=swap" rel="stylesheet">
<style>
  :root {
    --page: #ffffff;
    --rose: #c95a6a;
    --coral: #dd7a5e;
    --sun: #f1c93c;
    --amber: #e9a93a;
    --plum: #6b3f8f;
    --violet: #7a4a9a;
    --teal: #3fa59b;
    --leaf: #8ab84a;
    --grey-text: #6d6e71;
    --rule: #9a9a9a;
    --card-edge: #b8b8b8;
    --white: #ffffff;
  }
  * { margin: 0; padding: 0; box-sizing: border-box; }
  html, body {
    width: 1015px; height: 1200px; overflow: hidden;
    background: var(--page);
  }
  .sheet { position: relative; width: 1015px; height: 1200px; }

  .dimension, .side-label {
    position: absolute;
    font-family: "Roboto Condensed", sans-serif;
    font-style: italic; font-weight: 300;
    color: var(--grey-text);
    font-size: 34px;
  }
  .dimension-width { left: 110px; top: 268px; width: 380px; display: flex; align-items: center; gap: 22px; }
  .dimension-width .rule { flex: 1; height: 1px; background: var(--rule); }
  .dimension-height { left: 0; top: 370px; width: 96px; height: 608px; display: flex; flex-direction: column; align-items: center; gap: 20px; font-size: 30px; }
  .dimension-height .rule { flex: 1; width: 1px; background: var(--rule); }
  .dimension-height span { white-space: nowrap; }

  .card { position: absolute; top: 370px; width: 380px; height: 608px; display: block; }
  .card-front { left: 110px; outline: 1.5px solid var(--card-edge); }
  .card-back { left: 590px; }

  .side-label-front { left: 410px; top: 1000px; }
  .side-label-back { left: 880px; top: 1000px; }

  .brand-name { font-family: "Montserrat", sans-serif; font-weight: 600; fill: var(--grey-text); }
  .tagline-lead { font-family: "Baloo 2", sans-serif; font-weight: 700; fill: var(--sun); }
  .tagline-close { font-family: "Baloo 2", sans-serif; font-weight: 800; fill: var(--white); }
  .phone { font-family: "Source Sans 3", sans-serif; fill: var(--plum); }
  .phone-lead { font-weight: 700; }
  .person-first { font-family: "Source Sans 3", sans-serif; font-weight: 300; fill: var(--white); }
  .person-last { font-family: "Source Sans 3", sans-serif; font-weight: 700; font-style: italic; fill: var(--white); }
  .role { font-family: "Source Sans 3", sans-serif; font-weight: 400; fill: var(--white); }
  .contact-arc { font-family: "Source Sans 3", sans-serif; font-weight: 400; fill: var(--white); }
  .service-light { font-family: "Source Sans 3", sans-serif; font-weight: 400; fill: var(--sun); }
  .service-slab { font-family: "Alfa Slab One", serif; fill: var(--white); }
</style>
</head>
<body>
<main class="sheet">

  <div class="dimension dimension-width"><span class="rule"></span><span>50 mm</span><span class="rule"></span></div>
  <div class="dimension dimension-height"><span class="rule"></span><span>80 mm</span><span class="rule"></span></div>

  <svg class="card card-front" viewBox="0 0 420 672" xmlns="http://www.w3.org/2000/svg">
    <defs>
      <clipPath id="front-clip"><rect width="420" height="672"/></clipPath>
      <linearGradient id="front-arc-fill" x1="0" y1="1" x2="1" y2="0">
        <stop offset="0" stop-color="var(--teal)"/>
        <stop offset="0.35" stop-color="var(--leaf)"/>
        <stop offset="0.6" stop-color="var(--violet)"/>
        <stop offset="1" stop-color="var(--plum)"/>
      </linearGradient>
    </defs>
    <rect class="card-surface" width="420" height="672" fill="var(--white)"/>

    <g class="brand-lockup">
      <circle class="brand-mark" cx="210" cy="120" r="78" fill="var(--plum)"/>
      <text class="brand-name" x="210" y="262" text-anchor="middle" font-size="42">Woven Path</text>
      <text class="brand-name" x="210" y="314" text-anchor="middle" font-size="42">Wellness</text>
    </g>

    <g class="tagline-panel" clip-path="url(#front-clip)">
      <circle role="img" aria-label="Flowing colour artwork in teal, green and plum" cx="210" cy="712" r="262" fill="url(#front-arc-fill)"/>
      <text class="tagline-lead" x="210" y="505" text-anchor="middle" font-size="30" transform="rotate(-4 210 505)">The Journey</text>
      <text class="tagline-lead" x="200" y="530" text-anchor="middle" font-size="25">home</text>
      <text class="tagline-close" x="205" y="568" text-anchor="middle" font-size="32">starts</text>
      <text class="tagline-close" x="210" y="598" text-anchor="middle" font-size="32">with</text>
      <text class="tagline-close" x="210" y="640" text-anchor="middle" font-size="44" text-decoration="underline">you</text>
    </g>
  </svg>

  <svg class="card card-back" viewBox="0 0 420 672" xmlns="http://www.w3.org/2000/svg">
    <defs>
      <clipPath id="back-clip"><rect width="420" height="672"/></clipPath>
      <linearGradient id="back-field" x1="1" y1="0" x2="0" y2="1">
        <stop offset="0" stop-color="var(--leaf)"/>
        <stop offset="1" stop-color="var(--teal)"/>
      </linearGradient>
      <linearGradient id="back-disc" x1="0" y1="0" x2="0" y2="1">
        <stop offset="0" stop-color="var(--rose)"/>
        <stop offset="0.35" stop-color="var(--rose)"/>
        <stop offset="0.58" stop-color="var(--coral)"/>
        <stop offset="0.72" stop-color="var(--amber)"/>
        <stop offset="1" stop-color="var(--plum)"/>
      </linearGradient>
      <path id="arc-upper" d="M 80 -10 A 372 372 0 0 1 340 250"/>
      <path id="arc-lower" d="M 335 250 A 370 370 0 0 1 300 560"/>
    </defs>

    <rect class="card-surface" width="420" height="672" fill="url(#back-field)"/>

    <g class="colour-field" clip-path="url(#back-clip)">
      <circle role="img" aria-label="Flowing colour artwork in rose, amber and plum" cx="0" cy="336" r="340" fill="url(#back-disc)"/>
    </g>

    <g class="contact-arcs">
      <path d="M 104 42 l 0 -10 a 3 3 0 0 1 6 0 l 0 8 l 8 2 l -2 10 l -10 0 z" fill="var(--white)" transform="rotate(20 110 40)"/>
      <text class="contact-arc" font-size="15"><textPath href="#arc-upper" startOffset="20%">wovenpathwellness.example</textPath></text>
      <g transform="rotate(70 340 235)">
        <rect x="333" y="230" width="14" height="10" fill="none" stroke="var(--white)" stroke-width="1.6"/>
        <path d="M333 230 L340 236 L347 230" fill="none" stroke="var(--white)" stroke-width="1.4"/>
      </g>
      <text class="contact-arc" font-size="15"><textPath href="#arc-lower" startOffset="6%">daniel@wovenpathwellness.example</textPath></text>
    </g>

    <g class="phone-block">
      <rect x="22" y="232" width="22" height="44" rx="3" fill="none" stroke="var(--plum)" stroke-width="3"/>
      <rect x="32" y="242" width="18" height="14" fill="var(--plum)"/>
      <text class="phone phone-lead" x="121" y="230" text-anchor="end" font-size="27">0491</text>
      <text class="phone" x="121" y="256" text-anchor="end" font-size="27">372</text>
      <text class="phone" x="121" y="282" text-anchor="end" font-size="27">815</text>
    </g>

    <g class="identity-block">
      <text class="person-first" x="140" y="233" font-size="38">Daniel</text>
      <text class="person-last" x="140" y="272" font-size="38">Porthwick</text>
      <rect x="142" y="281" width="170" height="3" fill="var(--sun)"/>
      <text class="role" x="310" y="305" text-anchor="end" font-size="19">Health &amp; Wellbeing</text>
      <text class="role" x="310" y="327" text-anchor="end" font-size="19">Life Coach</text>
    </g>

    <g class="services-list">
      <text class="service-light" x="396" y="560" text-anchor="end" font-size="25">COACHING</text>
      <text class="service-slab" x="396" y="584" text-anchor="end" font-size="21">SEMINARS</text>
      <text class="service-light" x="396" y="610" text-anchor="end" font-size="25">WORKSHOPS</text>
      <text class="service-slab" x="396" y="634" text-anchor="end" font-size="21">PODCAST</text>
    </g>
  </svg>

  <div class="side-label side-label-front">Front</div>
  <div class="side-label side-label-back">Back</div>

</main>
</body>
</html>
```